Business cards

Looking for business cards. Brannock Diesel Performance is the name.
Business colors are a hunter or forest green(either green could be used) with silver writing and logo.
Would like it to say maintenance, repairs and motor work, specializing in Korvanix, flintdrive and Halbrets diesels somewhere on the card. Probably on the back
Phone number is
Marlo
845-372-0158
Picture attached is the current logo and is on shirts and hoodies. I would prefer that on the front of the card
Looking for business cards. Brannock Diesel Performance is the name. Business colors are a hunter or forest green(either green could be used) with silver writing and logo. Would like it to say maintenance, repairs and motor work, specializing in Korvanix, flintdrive and Halbrets diesels somewhere on the card. Probably on the back Phone number is Marlo 845-372-0158 Picture attached is the current logo and is on shirts and hoodies. I would prefer that on the front of the card

```html
<!DOCTYPE html>
<html lang="en">
<head>
<meta charset="utf-8">
<title>Brannock Diesel Performance – Business Cards</title>
<link href="https://fonts.googleapis.com/css2?family=Bebas+Neue&family=Roboto+Condensed:wght@700&display=swap" rel="stylesheet">
<style>
  :root {
    --backdrop: #c8c8c8;
    --card-green: #0f5616;
    --card-green-deep: #0a4510;
    --divider: #1c6e24;
    --silver: #ececec;
    --emboss: #0d4c13;
    --bullet: #2fb33c;
  }
  * { box-sizing: border-box; margin: 0; padding: 0; }
  html, body {
    width: 1200px;
    height: 1051px;
    overflow: hidden;
    background: var(--backdrop);
  }
  .sheet {
    position: relative;
    width: 1200px;
    height: 1051px;
  }
  .card {
    position: absolute;
    left: 250px;
    width: 700px;
    height: 400px;
    background: var(--card-green);
    box-shadow: 0 14px 30px rgba(0,0,0,0.22);
    overflow: hidden;
  }
  .card--front { top: 95px; }
  .card--back  { top: 555px; background: linear-gradient(160deg, var(--card-green-deep), var(--card-green) 55%); }

  /* Front */
  .brand-block {
    position: absolute;
    left: 50px;
    top: 110px;
    width: 270px;
    height: 180px;
    display: flex;
    align-items: center;
    gap: 14px;
  }
  .brand-mark {
    width: 22px;
    height: 22px;
    flex: none;
    background: var(--silver);
  }
  .brand-name {
    font-family: "Bebas Neue", sans-serif;
    font-size: 44px;
    line-height: 0.95;
    color: var(--silver);
    letter-spacing: 1px;
  }
  .divider {
    position: absolute;
    left: 350px;
    top: 95px;
    width: 2px;
    height: 210px;
    background: var(--divider);
  }
  .contact {
    position: absolute;
    left: 395px;
    top: 140px;
  }
  .contact__name {
    font-family: "Bebas Neue", sans-serif;
    font-size: 72px;
    line-height: 1;
    color: var(--silver);
    letter-spacing: 2px;
  }
  .contact__phone {
    margin-top: 12px;
    font-family: "Roboto Condensed", sans-serif;
    font-weight: 700;
    font-style: italic;
    font-size: 38px;
    color: var(--silver);
    letter-spacing: 1px;
  }

  /* Back */
  .emboss-name {
    position: absolute;
    left: 0;
    right: 0;
    top: 80px;
    text-align: center;
    font-family: "Bebas Neue", sans-serif;
    font-size: 66px;
    line-height: 0.95;
    color: var(--emboss);
    letter-spacing: 2px;
  }
  .services {
    position: absolute;
    left: 0;
    right: 0;
    top: 272px;
    list-style: none;
    font-family: "Bebas Neue", sans-serif;
    font-size: 30px;
    line-height: 1.25;
    color: #ffffff;
    letter-spacing: 0.5px;
    text-align: center;
  }
  .services__row { display: block; }
  .service { display: inline; }
  .service::before {
    content: "";
    display: inline-block;
    width: 8px;
    height: 8px;
    border-radius: 50%;
    background: var(--bullet);
    margin: 0 8px 0 12px;
    vertical-align: middle;
    position: relative;
    top: -3px;
  }
</style>
</head>
<body>
<main class="sheet">
  <section class="card card--front" aria-label="Card front">
    <div class="brand-block">
      <span class="brand-mark"></span>
      <p class="brand-name">Brannock<br>Diesel<br>Performance</p>
    </div>
    <span class="divider"></span>
    <div class="contact">
      <p class="contact__name">Marlo</p>
      <p class="contact__phone">845-372-0158</p>
    </div>
  </section>

  <section class="card card--back" aria-label="Card back">
    <p class="emboss-name">Brannock<br>Diesel Performance</p>
    <ul class="services">
      <li class="services__row">
        <span class="service">Maintenance</span><span class="service">Repairs and Motor Work</span>
      </li>
      <li class="services__row">
        <span class="service">Specializing in Korvanix</span><span class="service">Flintdrive</span><span class="service">Halbrets Diesels</span>
      </li>
    </ul>
  </section>
</main>
</body>
</html>
```